Photographic Business Card

I am a photographic artist and want a business card to reflect creativity. Two current websites of my photos are viewable at gloriouscoastlines.pixmerrow.com and quietharbourview.pixmerrow.com but a main website is under design at www.tjbrannock.com. I do not do weddings, I am not so much into portraits, I do a lot of landscapes, seascapes, My eventual website will be a gallery online from which I sell images, to be printed and framed.

Target Market(s)

Consumers in general, tourists, busineses

Industry/Entity Type

Business

Contact Information for Business Card

T J Brannock
Photographic Artist
Kettle Cove
BRANVALE, North Isles
owen@tjbrannock.com

Logo Text

open to suggestions

Font styles to use
Sans Serif
Script

Colors

Designer to choose colors to be used in the design.

Requirements
Must have
• my name and contact details
Nice to have
• a logo is to be designed separately
Should not have
• I am open to all suggestions

```html
<!DOCTYPE html>
<html lang="en">
<head>
<meta charset="utf-8">
<title>T J Brannock – Business Card</title>
<link rel="stylesheet" href="https://fonts.googleapis.com/css2?family=Michroma&family=Nunito+Sans:wght@400;600&display=swap">
<style>
  :root {
    --backdrop: #111111;
    --card: #2a2a2a;
    --card-edge: #363636;
    --white: #f2f2f2;
    --green: #4cb648;
    --silver: #b9b9b9;
    --ring-green: #14913a;
  }
  * { margin: 0; padding: 0; box-sizing: border-box; }
  html, body {
    width: 1200px;
    height: 900px;
    overflow: hidden;
    background: var(--backdrop);
  }
  .stage {
    position: relative;
    width: 1200px;
    height: 900px;
    display: flex;
    align-items: center;
    justify-content: center;
    gap: 40px;
  }
  .card {
    position: relative;
    width: 500px;
    height: 286px;
    background: var(--card);
    border: 1px solid var(--card-edge);
    border-radius: 3px;
    box-shadow: 0 18px 40px rgba(0,0,0,0.55);
  }

  /* Front */
  .card--front {
    display: flex;
    align-items: center;
    justify-content: center;
  }
  .front-mark {
    display: flex;
    align-items: center;
    gap: 14px;
  }
  .front-mark__dot {
    width: 22px;
    height: 22px;
    border-radius: 50%;
    border: 3px solid var(--ring-green);
  }
  .front-mark__name {
    font-family: "Michroma", sans-serif;
    font-size: 22px;
    letter-spacing: 3px;
    color: var(--white);
    text-transform: uppercase;
  }

  /* Back */
  .identity {
    position: absolute;
    left: 30px;
    top: 150px;
    width: 220px;
  }
  .identity__name {
    font-family: "Michroma", sans-serif;
    font-size: 16px;
    font-weight: 400;
    letter-spacing: 2.5px;
    color: var(--white);
    text-transform: uppercase;
    line-height: 1;
    white-space: nowrap;
  }
  .identity__role {
    font-family: "Michroma", sans-serif;
    font-size: 9px;
    letter-spacing: 1.5px;
    font-variant: small-caps;
    color: var(--green);
    margin-top: 4px;
  }
  .identity__rule {
    width: 182px;
    height: 2px;
    background: var(--white);
    margin-top: 6px;
  }
  .brand-mark {
    position: absolute;
    right: 34px;
    top: 64px;
    display: flex;
    align-items: center;
    gap: 8px;
  }
  .brand-mark__dot {
    width: 16px;
    height: 16px;
    border-radius: 50%;
    background: var(--silver);
  }
  .brand-mark__name {
    font-family: "Michroma", sans-serif;
    font-size: 12px;
    letter-spacing: 1.5px;
    color: var(--silver);
    text-transform: uppercase;
  }
  .contact {
    position: absolute;
    right: 30px;
    top: 186px;
    width: 190px;
    text-align: right;
    font-family: "Nunito Sans", sans-serif;
    font-size: 13px;
    line-height: 1.3;
    color: var(--white);
    font-style: normal;
  }
  .contact__rule {
    height: 2px;
    background: var(--white);
    margin-bottom: 10px;
  }
  .contact__line--spaced { margin-top: 6px; }
</style>
</head>
<body>
  <main class="stage">
    <section class="card card--front" aria-label="Card front">
      <div class="front-mark">
        <span class="front-mark__dot"></span>
        <span class="front-mark__name">T J Brannock</span>
      </div>
    </section>

    <section class="card card--back" aria-label="Card back">
      <div class="identity">
        <h1 class="identity__name">T J Brannock</h1>
        <p class="identity__role">Photographic Artist</p>
        <div class="identity__rule"></div>
      </div>

      <div class="brand-mark">
        <span class="brand-mark__dot"></span>
        <span class="brand-mark__name">T J Brannock</span>
      </div>

      <address class="contact">
        <div class="contact__rule"></div>
        <div class="contact__line">Kettle Cove</div>
        <div class="contact__line">BRANVALE, North Isles</div>
        <div class="contact__line contact__line--spaced">081-472-9158</div>
        <div class="contact__line">owen@tjbrannock.com</div>
      </address>
    </section>
  </main>
</body>
</html>
```